Trade Show Display

We need a design for a trade show pop up display. It should incorporate our colors and logo and should complement our other advertising pieces. Our primary brochure is uploaded. Also uploaded is a file with the text to be included and another file with the display dimensions.

```html
<!DOCTYPE html>
<html lang="en">
<head>
<meta charset="utf-8">
<title>Crestline Workforce – Trade Show Display</title>
<link href="https://fonts.googleapis.com/css2?family=Poppins:ital,wght@0,300;0,400;1,400&display=swap" rel="stylesheet">
<style>
  :root {
    --navy: #063a5c;
    --green: #8fb03e;
    --white: #ffffff;
    --backdrop: #e7e7e7;
    --photo-warm: #a36a42;
    --photo-dark: #1e2735;
  }
  * { margin: 0; padding: 0; box-sizing: border-box; }
  html, body {
    width: 1200px; height: 887px; overflow: hidden;
    background: var(--backdrop);
    font-family: "Poppins", Arial, sans-serif;
  }
  .display {
    position: absolute; left: 0; top: 42px;
    width: 913px; height: 610px;
    background: var(--white);
    transform: scale(1.3143);
    transform-origin: 0 0;
    overflow: hidden;
    color: var(--navy);
  }
  .shapes { position: absolute; inset: 0; width: 913px; height: 610px; }
  .brand {
    position: absolute; left: 48px; top: 112px;
    display: flex; align-items: center; gap: 14px;
  }
  .brand-dot {
    width: 50px; height: 50px; border-radius: 50%;
    background: var(--navy);
  }
  .brand-name {
    font-size: 23px; font-weight: 400; line-height: 1.05;
    color: var(--navy); letter-spacing: 0.5px;
  }
  .services {
    position: absolute; left: 110px; top: 212px;
    list-style: none;
  }
  .services li {
    display: flex; align-items: center; gap: 9px;
    font-size: 14.3px; line-height: 20.3px; height: 20.3px;
  }
  .services svg { width: 13px; height: 13px; flex: none; }
  .rule {
    position: absolute; left: 113px; top: 455px; width: 258px; height: 6px;
  }
  .tagline {
    position: absolute; left: 113px; top: 472px; width: 400px;
    font-size: 16.3px; font-style: italic; line-height: 22px;
  }
  .motto {
    position: absolute; left: 639px; top: 337px;
    font-size: 29px; font-weight: 300; line-height: 32px;
    color: var(--white);
  }
</style>
</head>
<body>
<main class="display">
  <svg class="shapes" viewBox="0 0 913 610" aria-hidden="false">
    <defs>
      <linearGradient id="photo-tone" x1="0" y1="0" x2="1" y2="0">
        <stop offset="0" stop-color="var(--photo-warm)"/>
        <stop offset="0.55" stop-color="#7a5a45"/>
        <stop offset="1" stop-color="var(--photo-dark)"/>
      </linearGradient>
    </defs>
    <!-- corner wave -->
    <path d="M0 0 H335 C300 45 240 62 150 70 C80 76 30 98 0 140 Z" fill="var(--navy)"/>
    <path d="M0 148 C30 104 82 84 155 78 C245 70 300 52 322 10" fill="none" stroke="var(--green)" stroke-width="1.2"/>
    <!-- photo area -->
    <rect x="390" y="30" width="315" height="425" rx="4" fill="url(#photo-tone)" role="img" aria-label="Photo of two business professionals reviewing a tablet together"/>
    <!-- navy swoosh -->
    <path d="M395 458 C470 440 520 410 560 350 C600 290 640 245 718 232 C700 270 660 300 620 340 C580 380 520 440 395 458 Z" fill="var(--navy)"/>
    <!-- motto circle -->
    <circle cx="729" cy="374" r="117" fill="none" stroke="var(--green)" stroke-width="1.2"/>
    <circle cx="722" cy="382" r="106" fill="var(--navy)"/>
    <!-- green swoosh -->
    <path d="M692 577 C790 560 830 520 860 470 C880 435 895 395 913 368 V440 C890 490 870 530 830 560 C790 585 740 583 692 577 Z" fill="var(--green)"/>
  </svg>

  <div class="brand">
    <span class="brand-dot"></span>
    <span class="brand-name">CRESTLINE<br>WORKFORCE</span>
  </div>

  <ul class="services">
    <li><svg viewBox="0 0 14 14"><circle cx="7" cy="7" r="7" fill="var(--green)"/><circle cx="7" cy="7" r="4.3" fill="var(--navy)"/><path d="M5 7.2 6.5 8.6 9.2 5.6" stroke="#fff" stroke-width="1.2" fill="none"/></svg>Talent Acquisition</li>
    <li><svg viewBox="0 0 14 14"><circle cx="7" cy="7" r="7" fill="var(--green)"/><circle cx="7" cy="7" r="4.3" fill="var(--navy)"/><path d="M5 7.2 6.5 8.6 9.2 5.6" stroke="#fff" stroke-width="1.2" fill="none"/></svg>Onboarding</li>
    <li><svg viewBox="0 0 14 14"><circle cx="7" cy="7" r="7" fill="var(--green)"/><circle cx="7" cy="7" r="4.3" fill="var(--navy)"/><path d="M5 7.2 6.5 8.6 9.2 5.6" stroke="#fff" stroke-width="1.2" fill="none"/></svg>Payroll</li>
    <li><svg viewBox="0 0 14 14"><circle cx="7" cy="7" r="7" fill="var(--green)"/><circle cx="7" cy="7" r="4.3" fill="var(--navy)"/><path d="M5 7.2 6.5 8.6 9.2 5.6" stroke="#fff" stroke-width="1.2" fill="none"/></svg>Benefits Management</li>
    <li><svg viewBox="0 0 14 14"><circle cx="7" cy="7" r="7" fill="var(--green)"/><circle cx="7" cy="7" r="4.3" fill="var(--navy)"/><path d="M5 7.2 6.5 8.6 9.2 5.6" stroke="#fff" stroke-width="1.2" fill="none"/></svg>Time and Attendance</li>
    <li><svg viewBox="0 0 14 14"><circle cx="7" cy="7" r="7" fill="var(--green)"/><circle cx="7" cy="7" r="4.3" fill="var(--navy)"/><path d="M5 7.2 6.5 8.6 9.2 5.6" stroke="#fff" stroke-width="1.2" fill="none"/></svg>Performance Management</li>
    <li><svg viewBox="0 0 14 14"><circle cx="7" cy="7" r="7" fill="var(--green)"/><circle cx="7" cy="7" r="4.3" fill="var(--navy)"/><path d="M5 7.2 6.5 8.6 9.2 5.6" stroke="#fff" stroke-width="1.2" fill="none"/></svg>Cafeteria/FSA/HRA Administration</li>
    <li><svg viewBox="0 0 14 14"><circle cx="7" cy="7" r="7" fill="var(--green)"/><circle cx="7" cy="7" r="4.3" fill="var(--navy)"/><path d="M5 7.2 6.5 8.6 9.2 5.6" stroke="#fff" stroke-width="1.2" fill="none"/></svg>Human Resource Administration,</li>
    <li><svg viewBox="0 0 14 14"><circle cx="7" cy="7" r="7" fill="var(--green)"/><circle cx="7" cy="7" r="4.3" fill="var(--navy)"/><path d="M5 7.2 6.5 8.6 9.2 5.6" stroke="#fff" stroke-width="1.2" fill="none"/></svg>Compliance Management,</li>
    <li><svg viewBox="0 0 14 14"><circle cx="7" cy="7" r="7" fill="var(--green)"/><circle cx="7" cy="7" r="4.3" fill="var(--navy)"/><path d="M5 7.2 6.5 8.6 9.2 5.6" stroke="#fff" stroke-width="1.2" fill="none"/></svg>and Consulting</li>
    <li><svg viewBox="0 0 14 14"><circle cx="7" cy="7" r="7" fill="var(--green)"/><circle cx="7" cy="7" r="4.3" fill="var(--navy)"/><path d="M5 7.2 6.5 8.6 9.2 5.6" stroke="#fff" stroke-width="1.2" fill="none"/></svg>COBRA Administration</li>
  </ul>

  <svg class="rule" viewBox="0 0 258 6" aria-hidden="true">
    <circle cx="3" cy="3" r="3" fill="var(--green)"/>
    <line x1="3" y1="3" x2="258" y2="3" stroke="var(--green)" stroke-width="1"/>
  </svg>

  <p class="tagline">Human Capital Management Solutions for the entire employee Lifecycle</p>

  <p class="motto">An<br>Essential<br>Part of<br>Business</p>
</main>
</body>
</html>
```